Religious Church Business Card Design

We need a business card design for our new pastor. We would like something warm and inviting. colors grape and white.
Updates

Church # 718-555-0143 and Cell # 718-555-0172

I also have a logo i tried to upload

Industry/Entity Type

Business

Contact Information for Business Card

Elder Mel Kinsey, Bethel Covenant Church, 2148 Pellham Road, Bronx, NY 10467, email: melkinsey@bethelcovenantchurch.example, www.bethelcovenantchurch.example

Colors
886aae

```html
<!DOCTYPE html>
<html lang="en">
<head>
<meta charset="utf-8">
<title>Elder Mel Kinsey – Business Card</title>
<link rel="stylesheet" href="https://fonts.googleapis.com/css2?family=Gabriela&display=swap">
<style>
  :root {
    --page: #ffffff;
    --grape: #8a6daf;
    --grape-light: #a38cc3;
    --grape-sheet: #9f86c0;
    --grape-edge: #9a80bc;
    --ink-light: #ffffff;
    --ink-dark: #141414;
    --rule: rgba(255, 255, 255, 0.45);
  }
  html, body {
    margin: 0;
    padding: 0;
    width: 1200px;
    height: 702px;
    overflow: hidden;
    background: var(--page);
    font-family: "Gabriela", Georgia, serif;
  }
  .canvas {
    position: relative;
    width: 1200px;
    height: 702px;
    background: var(--page);
  }
  .card {
    position: absolute;
    left: 49px;
    top: 49px;
    width: 1104px;
    height: 607px;
    background: var(--grape);
    overflow: hidden;
    color: var(--ink-light);
  }
  .logo-corner {
    position: absolute;
    left: 0;
    top: 0;
    width: 214px;
    height: 228px;
  }
  .logo-label {
    position: absolute;
    left: 8px;
    top: 70px;
    width: 180px;
    text-align: center;
    font-size: 26px;
    color: var(--ink-dark);
    transform: rotate(-46deg);
    letter-spacing: -0.5px;
    white-space: nowrap;
  }
  .identity {
    position: absolute;
    left: 29px;
    top: 0;
    width: 484px;
    text-align: center;
  }
  .person-name {
    position: absolute;
    left: -20px;
    width: 524px;
    top: 248px;
    margin: 0;
    font-size: 54px;
    font-weight: 400;
    white-space: nowrap;
  }
  .identity-rule {
    position: absolute;
    left: 0;
    top: 326px;
    width: 484px;
    height: 1px;
    background: var(--rule);
  }
  .church-name {
    position: absolute;
    left: 0;
    width: 484px;
    top: 338px;
    margin: 0;
    font-size: 32px;
    font-weight: 400;
  }
  .church-address {
    position: absolute;
    left: 0;
    width: 484px;
    top: 390px;
    margin: 0;
    font-size: 19px;
  }
  .note-stack {
    position: absolute;
    left: 573px;
    top: 49px;
    width: 445px;
    height: 546px;
  }
  .contact {
    position: absolute;
    left: 600px;
    top: 0;
    width: 405px;
    text-align: center;
  }
  .contact-heading {
    position: absolute;
    left: 0; width: 405px;
    top: 88px;
    margin: 0;
    font-size: 35px;
    font-weight: 400;
  }
  .contact-line {
    position: absolute;
    left: -20px; width: 445px;
    margin: 0;
    font-size: 19px;
    white-space: nowrap;
  }
  .contact-line.email { top: 170px; }
  .contact-line.cell { top: 226px; font-size: 22px; }
  .contact-rule {
    position: absolute;
    left: 79px;
    top: 291px;
    width: 247px;
    height: 1px;
    background: var(--rule);
  }
  .contact-line.web { top: 326px; }
  .contact-line.office { top: 384px; font-size: 22px; }
</style>
</head>
<body>
<div class="canvas">
  <section class="card">
    <svg class="logo-corner" viewBox="0 0 214 228" aria-hidden="true">
      <polygon points="0,0 214,0 0,228" fill="#ffffff"/>
    </svg>
    <div class="logo-label">LOGO HERE</div>

    <div class="identity">
      <h1 class="person-name">Elder Mel Kinsey</h1>
      <div class="identity-rule"></div>
      <h2 class="church-name">Bethel Covenant Church</h2>
      <p class="church-address">2148 Pellham Road, Bronx, NY 10467</p>
    </div>

    <svg class="note-stack" viewBox="0 0 445 546" role="img" aria-label="Illustration of a stack of note papers with a pen">
      <rect x="4" y="14" width="432" height="526" rx="14" fill="var(--grape-edge)"/>
      <rect x="16" y="4" width="418" height="520" rx="10" fill="var(--grape-light)" opacity="0.7"/>
      <rect x="24" y="12" width="400" height="512" rx="6" fill="var(--grape-sheet)"/>
    </svg>

    <div class="contact">
      <h3 class="contact-heading">Contact Us</h3>
      <p class="contact-line email">melkinsey@bethelcovenantchurch.example</p>
      <p class="contact-line cell">Cell No. 718-555-0172</p>
      <div class="contact-rule"></div>
      <p class="contact-line web">www.bethelcovenantchurch.example</p>
      <p class="contact-line office">Church No. 718-555-0143</p>
    </div>
  </section>
</div>
</body>
</html>
```